Sons 1st B-Day Invitation Card

Hello, My son will be turning 1 next month. I want to create a creative invitation card. I will like my sons head to be used as a cartoon, maybe as a baby superhero, maybe with animals. I think that would be super cute. The imagination and creativity are endless. I will like my sons head to be in the form of a superhero but it's not Mandatory. His face doesn't have to be used. I will just like a nice fun and creative B-Day Invitation Card.

The card should have the following information. Address :Hop Zone Fun 47-12 Marlow Ave Astoria, NY 1110Event date: Sun, Sep 22, 2019 Event time: 4:30 PM - 8:30 PMDress Code- Please wear sock; they are required to use the facilityRSVP- Tunde Okorafor 347-712-8487VERY IMPORTANT- Liability forms must be signed by a parent or guardian, Please sign waiver in advance at https://hopzonefun.qrvevent.com/waivers.

Font styles to use
Sans Serif

Colors

Designer to choose colors to be used in the design.

Requirements
Must have
• I will like my sons head to be in the form of a superhero but it's not Mandatory. His face doesn't have to be used. I will just like a nice fun and creative B-Day Invitation Card

```html
<!DOCTYPE html>
<html lang="en">
<head>
<meta charset="utf-8">
<title>First Birthday Invitation</title>
<link rel="stylesheet" href="https://fonts.googleapis.com/css2?family=Amatic+SC:wght@700&family=Dancing+Script:wght@700&family=Lato:wght@400&display=swap">
<style>
  :root {
    --backdrop: #3a3430;
    --card-teal: #48afa5;
    --cloud-white: #f4fbfb;
    --cloud-shade: #d3eceb;
    --ink-white: #ffffff;
    --title-shadow: #2f7f77;
    --swirl-green: #8fcf8e;
    --cape-yellow: #f2c531;
    --bunting-pink: #ee5f8a;
    --bunting-blue: #4f5aa8;
    --bunting-teal: #35b6b0;
  }
  * { margin: 0; padding: 0; box-sizing: border-box; }
  html, body { width: 1120px; height: 1200px; overflow: hidden; background: var(--backdrop); }
  .canvas { position: relative; width: 1120px; height: 1200px; }
  .card {
    position: absolute; left: 150px; top: 30px; width: 820px; height: 1140px;
    background: var(--card-teal); overflow: hidden;
  }
  .clouds { position: absolute; left: 0; top: 0; width: 820px; height: 300px; }
  .bunting {
    position: absolute; left: 0; top: 0; width: 820px; height: 120px;
    background: linear-gradient(90deg, var(--cape-yellow) 0%, var(--bunting-teal) 35%, var(--bunting-blue) 60%, var(--bunting-pink) 100%);
    clip-path: polygon(0 8%, 50% 0, 100% 15%, 100% 55%, 90% 100%, 80% 55%, 70% 95%, 60% 45%, 50% 85%, 40% 50%, 30% 100%, 20% 60%, 10% 100%, 0 60%);
    opacity: 0.9;
  }
  .invited {
    position: absolute; left: 0; top: 78px; width: 820px; text-align: center;
    font-family: "Amatic SC", sans-serif; font-size: 50px; color: var(--ink-white);
    letter-spacing: 1px;
  }
  .hero-art {
    position: absolute; left: 150px; top: 140px; width: 530px; height: 420px;
    border-radius: 50%;
    background: radial-gradient(circle at 50% 55%, #e9b97a 0 14%, var(--cape-yellow) 15% 40%, var(--swirl-green) 41% 65%, rgba(143,207,142,0) 72%);
  }
  .title {
    position: absolute; left: 0; top: 490px; width: 820px; height: 250px;
    font-family: "Dancing Script", cursive; font-weight: 700; color: var(--ink-white);
    text-shadow: 3px 3px 0 var(--title-shadow);
  }
  .title-my { position: absolute; left: 225px; top: 0; font-size: 110px; line-height: 1; }
  .title-birthday { position: absolute; left: 0; top: 85px; width: 800px; text-align: center; font-size: 150px; line-height: 1; }
  .details { position: absolute; left: 195px; top: 770px; width: 420px; height: 240px; }
  .timeline { position: absolute; left: 0; top: 0; }
  .details p {
    position: absolute; left: 30px; font-family: "Amatic SC", sans-serif;
    color: var(--ink-white); line-height: 1; white-space: nowrap;
  }
  .venue { top: 10px; font-size: 32px; }
  .venue-line2 { top: 50px; font-size: 32px; }
  .date { top: 100px; font-size: 40px; }
  .time { top: 148px; font-size: 40px; }
  .rsvp { top: 200px; font-size: 38px; }
  .dress-badge { position: absolute; left: 530px; top: 810px; width: 140px; height: 140px; }
  .dress-badge text { font-family: "Amatic SC", sans-serif; fill: var(--card-teal); font-size: 17px; }
  .notice {
    position: absolute; left: 40px; top: 1070px; width: 740px; text-align: center;
    font-family: "Lato", sans-serif; font-size: 16.5px; line-height: 1.3; color: var(--ink-white);
  }
</style>
</head>
<body>
<div class="canvas">
  <section class="card">
    <svg class="clouds" viewBox="0 0 820 300" aria-hidden="true">
      <g fill="var(--cloud-shade)">
        <rect x="0" y="0" width="820" height="80"/>
        <circle cx="40" cy="120" r="70"/>
        <circle cx="150" cy="110" r="60"/>
        <circle cx="300" cy="60" r="55"/>
        <circle cx="640" cy="70" r="60"/>
        <circle cx="760" cy="150" r="80"/>
        <circle cx="800" cy="260" r="50"/>
      </g>
      <g fill="var(--cloud-white)">
        <circle cx="20" cy="100" r="50"/>
        <circle cx="130" cy="90" r="42"/>
        <circle cx="290" cy="40" r="40"/>
        <circle cx="650" cy="50" r="42"/>
        <circle cx="780" cy="130" r="58"/>
      </g>
    </svg>
    <div class="bunting" role="img" aria-label="Colourful bunting flags strung across the top"></div>

    <h1 class="invited">YOU ARE INVITED TO</h1>

    <div class="hero-art" role="img" aria-label="Illustration of the birthday boy flying as a baby superhero in a yellow cape, surrounded by a green swirl"></div>

    <h2 class="title">
      <span class="title-my">my</span>
      <span class="title-birthday">birthday</span>
    </h2>

    <div class="details">
      <svg class="timeline" width="24" height="240" viewBox="0 0 24 240" aria-hidden="true">
        <line x1="12" y1="0" x2="12" y2="236" stroke="var(--ink-white)" stroke-width="3"/>
        <circle cx="12" cy="26" r="7" fill="var(--ink-white)"/>
        <circle cx="12" cy="120" r="7" fill="var(--ink-white)"/>
        <circle cx="12" cy="168" r="7" fill="var(--ink-white)"/>
        <circle cx="12" cy="220" r="7" fill="var(--ink-white)"/>
      </svg>
      <p class="venue">At: Hop Zone Fun 47-12 Marlow</p>
      <p class="venue-line2">Ave Astoria, NY 1110</p>
      <p class="date">Sun, Sep 22, 2019</p>
      <p class="time">4:30 PM - 8:30</p>
      <p class="rsvp">RSVP- Tunde Okorafor 347-555-0193</p>
    </div>

    <svg class="dress-badge" viewBox="0 0 150 150" aria-label="Dress code: please wear socks">
      <polygon fill="var(--ink-white)" points="75,0 86,30 112,10 108,42 142,36 122,62 150,75 122,88 142,114 108,108 112,140 86,120 75,150 64,120 38,140 42,108 8,114 28,88 0,75 28,62 8,36 42,42 38,10 64,30"/>
      <g transform="rotate(-20 75 75)">
        <text x="75" y="70" text-anchor="middle">Dress Code</text>
        <text x="75" y="90" text-anchor="middle">Please wear sock</text>
      </g>
    </svg>

    <p class="notice">VERY IMPORTANT:<br>Liability forms must be signed by a parent or guardian, Please sign waiver in advance at<br>https://hopzonefun.qrvevent.com/waivers</p>
  </section>
</div>
</body>
</html>
```